Digital Medical Care Start-up: New Web Design Needed

We are a startup in Boston, USA. Our current website has mostly acceptable content but looks outdated and it is ineffective. Viewers - especially possible investors - are turned off. It may also have too much content - especially the table. Current site Https://CareLoomKits.com

Business: we produce apps for surgeons to give their patients. The apps describe the medical procedure they will have, how to prepare, what to do to speed recovery, and how to interpret any symptoms. One app for each medical procedure - there are over 200.

LIKES
https://www.finchwellness.com/
https://www.marlowcareworks.com/en/
https://vintrasa.com/about/
DISLIKES
https://tolvo-rex.com/
https://www.quenbridgely.com/
https://www.harrow-clinica.net/
https://www.zelvix.com/

Target Market(s)

Audience: Medical Surgeons (customers) and Investors (we will do our first capital raise afterward the new website) in USA.

Coding

Number of Pages Required

2 page

Font styles to use
Other font styles liked:
• Candara

Colors
0455a3
f37122

Requirements
Must have
• OUTPUT:
We want a fully Responsive Version.
We do not use Wordpress. The page layout (or template) should be html + css + images + a little JavaScript.
The first page is the landing page. The second page would be the template on which we put the remaining content.
After delivery, the html would be merged into the existing framework. The site needs to be built on a template so it can be managed by an average quasi-tech person, without the need for a coder.

See exisiting company and product logos. They will remain unchanged, so make sure the website is compatable with the current logos.
Nice to have
• We have attached an idea of ours. This is meant for your stimulation, not necessarily for replication. Our attachment does not have all the content details, but the outline is correct.

```html
<!DOCTYPE html>
<html lang="en">
<head>
<meta charset="utf-8">
<title>CareLoomKits – Procedure eCare</title>
<link rel="stylesheet" href="https://fonts.googleapis.com/css2?family=Hind:wght@400;500;600;700&display=swap">
<style>
:root{
  --orange:#ec5d1f;
  --orange-dark:#d24e15;
  --blue:#0b4a9c;
  --blue-deep:#063a86;
  --link-blue:#0d4f9e;
  --ink:#333;
  --muted:#555;
  --line:#d9d9d9;
  --white:#fff;
}
*{margin:0;padding:0;box-sizing:border-box}
html,body{width:1200px;height:3542px;overflow:hidden}
body{font-family:"Hind",sans-serif;color:var(--ink);background:var(--white);position:relative}
.abs{position:absolute}

/* header */
.site-header{position:absolute;top:0;left:0;width:1200px;height:85px;background:var(--white)}
.brand{position:absolute;left:111px;top:18px;display:flex;align-items:center;gap:10px}
.brand-dot{width:48px;height:48px;border-radius:50%;background:var(--link-blue)}
.brand-name{font-size:30px;font-weight:600;color:var(--link-blue);letter-spacing:.2px}
.main-nav{position:absolute;top:31px;left:436px;display:flex;gap:30px;font-size:14.5px}
.main-nav a{color:var(--ink);text-decoration:none}
.main-nav a.active{color:var(--orange)}

/* hero */
.hero{position:absolute;top:85px;left:0;width:1200px;height:624px;overflow:hidden}
.hero-photo{position:absolute;left:0;top:0;width:762px;height:624px;background:linear-gradient(120deg,#c9c3bb 0%,#e6e1da 45%,#b9b0a6 75%,#4d5566 100%)}
.hero-panel{position:absolute;left:762px;top:0;width:438px;height:624px;background:var(--orange)}
.hero-panel svg{position:absolute;left:0;top:0}
.hero-copy{position:absolute;left:784px;top:155px;color:var(--white)}
.hero-kicker{font-size:22px;letter-spacing:9px;line-height:45px;font-weight:400}
.hero-title{font-size:41px;font-weight:700;line-height:48px;margin-top:-2px}
.hero-sub{font-size:16px;font-weight:600;line-height:25px;margin-top:6px;padding-left:2px}
.hero-btn{position:absolute;left:786px;top:366px;width:201px;height:44px;border:2px solid var(--white);color:var(--white);font-weight:700;font-size:16px;letter-spacing:5px;display:flex;align-items:center;justify-content:center}
.dots{position:absolute;display:flex;gap:5px}
.dots span{width:14px;height:14px;border-radius:50%;border:1.5px solid var(--white)}
.dots span.on{background:var(--white)}

/* headings */
.section-head{position:absolute;left:0;width:1200px;text-align:center;font-weight:700;line-height:37px}
.section-head .hot{color:var(--orange);font-size:24px;display:block}
.section-head .cool{color:#3a3a3a;font-size:24px;display:block}

/* feature cards */
.feature-card{position:absolute;top:873px;width:319px;height:257px;border:1px solid var(--line);text-align:center;padding:44px 22px 0}
.feature-card h3{font-size:21px;font-weight:500;color:#3a3a3a;margin-bottom:14px}
.feature-card p{font-size:12.5px;line-height:19.5px;color:var(--muted)}
.feature-card a{display:inline-block;margin-top:14px;font-size:12.5px;font-weight:600;color:var(--ink);text-decoration:underline}
.feature-card.highlight{background:var(--orange);border-color:var(--orange);box-shadow:0 2px 8px rgba(0,0,0,.25)}
.feature-card.highlight h3,.feature-card.highlight p,.feature-card.highlight a{color:var(--white)}

/* benefits */
.team-photo{position:absolute;left:111px;top:1299px;width:356px;height:458px;background:linear-gradient(180deg,#d8dde3 0%,#7f96b8 45%,#3f63a8 75%,#2c3440 100%)}
.benefits{position:absolute;left:500px;top:1310px;width:560px}
.benefit{height:90.5px}
.benefit h4{font-size:16px;font-weight:700;color:var(--link-blue);line-height:22px}
.benefit p{font-size:12.3px;line-height:17.5px;color:var(--muted);margin-top:4px}

/* testimonials */
.testimonials{position:absolute;top:1856px;left:0;width:1200px;height:441px;background:radial-gradient(circle at 70% 40%,#1a5fb8 0%,var(--blue) 45%,var(--blue-deep) 100%)}
.portrait{position:absolute;left:113px;top:89px;width:250px;height:250px;border-radius:50%;background:radial-gradient(circle at 50% 45%,#d9b9a0 0%,#b89479 45%,#8b8f99 100%)}
.quote-mark{position:absolute;left:162px;top:268px;font-size:120px;line-height:1;color:var(--orange);font-weight:700}
.testi-copy{position:absolute;left:425px;top:52px;width:620px;color:var(--white)}
.testi-copy h2{font-size:24px;font-weight:700;margin-bottom:16px}
.testi-copy blockquote{font-size:15px;line-height:22px}
.testi-copy .who{font-size:17.5px;font-weight:700;margin-top:16px}
.testi-copy .role{font-size:13px;line-height:26.5px}

/* clinical groups */
.group-card{position:absolute;width:319px;height:257px;border:1px solid var(--line);text-align:center}
.group-img{position:absolute;left:81px;top:-78px;width:156px;height:156px;border-radius:50%}
.group-card h3{position:absolute;top:105px;left:0;width:100%;font-size:20px;font-weight:500;color:#222;letter-spacing:.5px}
.group-card .doc{position:absolute;top:152px;left:0;width:100%;font-size:13.5px;line-height:26.5px;color:var(--ink)}
.group-card .doc b{font-weight:600}

/* footer */
.site-footer{position:absolute;top:3256px;left:0;width:1200px;height:286px;background:var(--blue);color:var(--white)}
.foot-brand{position:absolute;left:113px;top:44px;display:flex;align-items:center;gap:10px}
.foot-brand .brand-dot{background:var(--white);width:46px;height:46px}
.foot-brand .brand-name{color:var(--white)}
.socials{position:absolute;left:168px;top:100px;display:flex;gap:4px}
.socials span{width:30px;height:30px;border-radius:50%;background:var(--white)}
.foot-col h5{font-size:15px;font-weight:600;letter-spacing:.3px}
.contact-col{position:absolute;left:476px;top:30px}
.contact-row{display:flex;align-items:center;gap:14px;font-size:17px;font-weight:600;height:39px}
.contact-col h5{margin-bottom:8px}
.news-col{position:absolute;left:837px;top:30px;width:250px}
.news-col p{font-size:12.5px;line-height:21px;margin-top:12px}
.news-input{margin-top:10px;height:43px;border:1px solid var(--white);display:flex;align-items:center;gap:10px;padding-left:12px;font-size:14px}
.foot-rule{position:absolute;left:111px;top:223px;width:977px;height:1px;background:rgba(255,255,255,.5)}
.legal{position:absolute;top:238px;left:0;width:1200px;text-align:center;font-size:13.5px}
</style>
</head>
<body>

<header class="site-header">
  <div class="brand"><span class="brand-dot"></span><span class="brand-name">CARELOOMKITS</span></div>
  <nav class="main-nav">
    <a class="active" href="#">Home</a><a href="#">About Us</a><a href="#">Medical Advisory Board</a><a href="#">Clinical Groups</a><a href="#">Testimonials</a><a href="#">Contact Us</a>
  </nav>
</header>

<section class="hero">
  <div class="hero-photo" role="img" aria-label="Man relaxing on a sofa holding a tablet showing the app"></div>
  <div class="hero-panel">
    <svg width="438" height="624" viewBox="0 0 438 624">
      <polygon points="0,0 90,0 330,200 438,350 438,560 220,470" fill="var(--orange-dark)" opacity=".55"/>
    </svg>
  </div>
  <div class="hero-copy">
    <div class="hero-kicker">DIGITALLY</div>
    <div class="hero-kicker">DELIVERING</div>
    <div class="hero-title">Procedure eCare</div>
    <div class="hero-sub">for 100+ procedures<br>Quickly and economically</div>
  </div>
  <div class="hero-btn">CONTACT US</div>
  <div class="dots" style="left:792px;top:447px"><span class="on"></span><span></span><span></span></div>
</section>

<div class="section-head" style="top:772px"><span class="hot">WE ENABLE CLINICIANS TO INCREASE</span><span class="cool">THE NUMBER OF PROCEDURES - WHILE IMPROVING HEALTH OUTCOMES</span></div>

<article class="feature-card" style="left:111px"><h3>Periop Tasks</h3><p>Lorem Ipsum is simply dummy text of the printing and typesetting industry. Lorem Ipsum has been the industry's standard dummy text ever since the 1500s,</p><a href="#">Read More</a></article>
<article class="feature-card highlight" style="left:440px"><h3>Interactive SYMPTOM TRIAGE</h3><p>Lorem Ipsum is simply dummy text of the printing and typesetting industry. Lorem Ipsum has been the industry's standard dummy text ever since the 1500s,</p><a href="#">Read More</a></article>
<article class="feature-card" style="left:769px"><h3>Communications</h3><p>Lorem Ipsum is simply dummy text of the printing and typesetting industry. Lorem Ipsum has been the industry's standard dummy text ever since the 1500s,</p><a href="#">Read More</a></article>

<div class="section-head" style="top:1198px"><span class="hot">WE HAVE THE BEST ECARE</span><span class="cool">SOLUTION FOR SURGERIES AND TREATMENT</span></div>

<div class="team-photo" role="img" aria-label="Group of smiling doctors and nurses in scrubs standing in a hospital corridor"></div>
<div class="benefits">
  <div class="benefit"><h4>Immediate and Measurable Benefits</h4><p>Lorem Ipsum is simply dummy text of the printing and typesetting industry. Lorem Ipsum<br>has been the industry's standard dummy text ever since the 1500s,</p></div>
  <div class="benefit"><h4>Improvement In the entire Patient journey</h4><p>Lorem Ipsum is simply dummy text of the printing and typesetting industry. Lorem Ipsum<br>has been the industry's standard dummy text ever since the 1500s,</p></div>
  <div class="benefit"><h4>Provider Specific</h4><p>Lorem Ipsum is simply dummy text of the printing and typesetting industry. Lorem Ipsum<br>has been the industry's standard dummy text ever since the 1500s,</p></div>
  <div class="benefit"><h4>Accessible From Any Device</h4><p>Lorem Ipsum is simply dummy text of the printing and typesetting industry. Lorem Ipsum<br>has been the industry's standard dummy text ever since the 1500s,</p></div>
  <div class="benefit"><h4>No User Manual Needed</h4><p>Lorem Ipsum is simply dummy text of the printing and typesetting industry. Lorem Ipsum<br>has been the industry's standard dummy text ever since the 1500s,</p></div>
</div>

<section class="testimonials">
  <div class="portrait" role="img" aria-label="Portrait of the quoted surgeon"></div>
  <div class="quote-mark">“</div>
  <div class="testi-copy">
    <h2>TESTIMONIALS</h2>
    <blockquote>"The CareLoomKits Peri-op eCare app provides patients with critical information about their diagnosis and treatment. This service guides patients through what is often a very stressful experience, answering common questions that arise during the course of treatment. It's a fantastic support tool for both doctors and patients."</blockquote>
    <div class="who">Martin R. Hale, MD</div>
    <div class="role">Associate Professor, Orthopaedic Surgery<br>Eastbrook Medical School<br>Calder Women's Hospital</div>
  </div>
  <div class="dots" style="left:573px;top:368px"><span class="on"></span><span></span><span></span></div>
</section>

<div class="section-head" style="top:2364px"><span class="hot">CLINICAL GROUPS</span></div>

<article class="group-card" style="left:111px;top:2530px"><div class="group-img" role="img" aria-label="Stomach illustration" style="background:radial-gradient(circle at 50% 45%,#e0653f,#a8301c 60%,#6e1a12)"></div><h3>BARIATRIC</h3><div class="doc"><b>Owen T. Reyes, MD MS FACS</b><br>Professor of Surgery<br>Eastbrook Medical School</div></article>
<article class="group-card" style="left:440px;top:2530px"><div class="group-img" role="img" aria-label="Heart illustration" style="background:radial-gradient(circle at 50% 50%,#7fb6f2,#2e6fcf 55%,#173f8a)"></div><h3>CARDIAC SURGERY</h3><div class="doc"><b>Owen T. Reyes, MD MS FACS</b><br>Professor of Surgery<br>Eastbrook Medical School</div></article>
<article class="group-card" style="left:769px;top:2530px"><div class="group-img" role="img" aria-label="Fetus in womb illustration" style="background:radial-gradient(circle at 50% 50%,#d64b2a,#5a1f2c 40%,#0c1530 75%)"></div><h3>FERTILITY MEDICINE</h3><div class="doc"><b>Owen T. Reyes, MD MS FACS</b><br>Professor of Surgery<br>Eastbrook Medical School</div></article>

<article class="group-card" style="left:111px;top:2912px"><div class="group-img" role="img" aria-label="Hands holding a test strip" style="background:radial-gradient(circle at 50% 50%,#fbe3e6,#f4b8c1 60%,#e79aa6)"></div><h3>GYNECOLOGY</h3><div class="doc"><b>Owen T. Reyes, MD MS FACS</b><br>Professor of Surgery<br>Eastbrook Medical School</div></article>
<article class="group-card" style="left:440px;top:2912px"><div class="group-img" role="img" aria-label="Organ anatomy illustration" style="background:linear-gradient(135deg,#4d8fe0 0%,#d92c45 45%,#b8142e 70%,#3f7bd6 100%)"></div><h3>MINIMALLY INVASIVE</h3><div class="doc"><b>Owen T. Reyes, MD MS FACS</b><br>Professor of Surgery<br>Eastbrook Medical School</div></article>
<article class="group-card" style="left:769px;top:2912px"><div class="group-img" role="img" aria-label="Pregnant belly with hands" style="background:radial-gradient(circle at 45% 50%,#e8c2a8,#c48d6c 60%,#8a5c45)"></div><h3>OBSTETRICS</h3><div class="doc"><b>Owen T. Reyes, MD MS FACS</b><br>Professor of Surgery<br>Eastbrook Medical School</div></article>

<footer class="site-footer">
  <div class="foot-brand"><span class="brand-dot"></span><span class="brand-name">CARELOOMKITS</span></div>
  <div class="socials"><span></span><span></span><span></span><span></span></div>

  <div class="foot-col contact-col">
    <h5>CONTACT</h5>
    <div class="contact-row">
      <svg width="24" height="22" viewBox="0 0 24 22" fill="none" stroke="#fff" stroke-width="1.6"><path d="M4 2l4 1 1 5-2 2c1.5 3 3.5 5 6.5 6.5l2-2 5 1 1 4c-1 1.5-3 2-5 1.5C10 18 4.5 12.5 3 6.5 2.5 4.5 3 3 4 2z"/><path d="M14 2a7 7 0 0 1 7 7M14 6a3 3 0 0 1 3 3"/></svg>
      <span>+ 617-555-0148</span></div>
    <div class="contact-row">
      <svg width="22" height="16" viewBox="0 0 22 16" fill="none" stroke="#fff" stroke-width="1.6"><rect x="1" y="1" width="20" height="14"/><path d="M1 1l10 8 10-8M1 15l7-6M21 15l-7-6"/></svg>
      <span>contactus@careloomkitsinc.com</span></div>
    <div class="contact-row">
      <svg width="22" height="22" viewBox="0 0 22 22"><path d="M11 1a7 7 0 0 0-7 7c0 5 7 13 7 13s7-8 7-13a7 7 0 0 0-7-7z" fill="#fff"/><circle cx="11" cy="8" r="2.6" fill="var(--blue)"/></svg>
      <span>CareLoomKits Inc, Boston, USA</span></div>
  </div>

  <div class="foot-col news-col">
    <h5>SIGN UP FOR NEWSLETTER</h5>
    <p>Neque porro quisquam est qui dolorem ipsum quia dolor sit</p>
    <div class="news-input">
      <svg width="38" height="20" viewBox="0 0 38 20" fill="none" stroke="#fff" stroke-width="1.4"><path d="M1 6h8M3 10h6M5 14h4"/><rect x="12" y="2" width="24" height="16"/><path d="M12 2l12 9 12-9"/></svg>
      <span>Enter your Email</span>
    </div>
  </div>

  <div class="foot-rule"></div>
  <div class="legal">©2021 CareLoomKits Inc., CareLoomKits™ and CareLoomKits Inc™ are trademarks of CareLoomKits Inc. &nbsp;Privacy Policy &nbsp;| &nbsp;Terms of Use &nbsp;| &nbsp;Login</div>
</footer>

</body>
</html>
```